Clean, creative business Wordpress Site

Our company is building a website via Wordpress and needs a clean, no fuss, modern looking design that reflects our company brand (see attached logos).

In addition, the company is a woman owned business (no middle-aged white guy stock photos please) and primarily works with the oil & gas industry. We would prefer no images with direct references to energy (rigs, windmills, solar panels, etc.). Part of our consulting is providing thought leadership around energy politics and policy so creative ways to incorporate that visually will be appreciated as well.

Site map of pages below:

Home
- About
- Team
- Expertise
- Blog

We prefer a header image that includes the company logo and easy to identify and navigate menus.

Target Market(s)

Energy professionals, Executives

Industry/Entity Type

Consulting

Font styles to use
Serif

Colors
85acd3
0255a3
cedeed
ffffff

Requirements
Must have
• Clean and easy to navigate, clear menus, simple design that reflects company logo.

```html
<!DOCTYPE html>
<html lang="en">
<head>
<meta charset="utf-8">
<title>Ironvale Energy</title>
<link href="https://fonts.googleapis.com/css2?family=Montserrat:wght@400;600;700&family=Questrial&display=swap" rel="stylesheet">
<style>
:root{
  --blue:#0255a3;
  --blue-mid:#2f6fb3;
  --sky:#85acd3;
  --ice:#cedeed;
  --white:#ffffff;
  --ink:#222222;
  --grey:#777777;
  --line:#e3e3e3;
  --pale:#f2f2f2;
}
*{margin:0;padding:0;box-sizing:border-box}
html,body{width:1200px;height:3041px;overflow:hidden;background:var(--white)}
body{font-family:"Questrial",sans-serif;color:var(--ink);position:relative}
section,header,footer{position:absolute;left:0;width:1200px}
.abs{position:absolute}
.center{text-align:center;left:0;width:1200px}

/* header */
.site-header{top:0;height:115px;background:var(--white);box-shadow:0 2px 6px rgba(0,0,0,.08);z-index:2}
.brand{left:100px;top:32px;display:flex;align-items:center;gap:14px}
.brand-mark{width:46px;height:46px;border-radius:50%;background:var(--blue)}
.brand-name{font-family:"Questrial",sans-serif;font-size:36px;color:var(--blue);letter-spacing:1px}
.main-nav{right:98px;top:50px;display:flex;gap:42px;font-size:15px;color:var(--ink)}
.main-nav a{color:inherit;text-decoration:none}
.main-nav .active{color:var(--blue)}

/* hero */
.hero{top:115px;height:503px}
.hero-photo{position:absolute;inset:0;background:linear-gradient(100deg,#b9c2c9 0%,#d8d6cf 30%,#4a4a55 45%,#c9a26a 52%,#c7ced3 70%,#6f93b0 100%)}
.hero-title{top:158px;font-family:"Montserrat",sans-serif;font-weight:700;font-size:58px;color:var(--white);text-shadow:0 2px 6px rgba(0,0,0,.35);letter-spacing:1px}
.hero-sub{top:228px;font-size:21px;color:var(--white);text-shadow:0 1px 4px rgba(0,0,0,.4)}
.btn-solid{left:490px;top:288px;width:220px;height:54px;background:var(--blue);color:var(--white);font-family:"Montserrat",sans-serif;font-weight:600;font-size:18px;line-height:54px;text-align:center;border-radius:3px}
.slider-dots{left:560px;top:451px;display:flex;gap:6px}
.slider-dots span{width:17px;height:17px;border-radius:50%;background:var(--white)}
.slider-dots span:first-child{background:transparent;border:2px solid var(--white)}

/* welcome */
.welcome{top:618px;height:562px}
.section-title{font-family:"Montserrat",sans-serif;font-weight:700;font-size:33px;color:var(--ink)}
.section-title em{font-style:normal;color:var(--blue)}
.welcome .section-title{top:52px}
.welcome-lead{top:100px;left:200px;width:800px;font-size:14px;line-height:27px;color:var(--grey);text-align:center}
.card{top:247px;width:308px;height:240px;border:1px solid var(--line);background:var(--white);text-align:center}
.card-icon{position:absolute;left:92px;top:-65px;width:124px;height:124px;border-radius:50%;background:var(--blue);border:6px solid var(--white);box-shadow:0 0 0 1px var(--line);display:flex;align-items:center;justify-content:center}
.card h3{margin-top:82px;font-weight:400;font-size:17px;letter-spacing:.5px;color:var(--ink)}
.card p{margin:16px auto 0;width:230px;font-size:12px;line-height:20px;color:var(--grey)}
.read-more{display:inline-block;margin-top:18px;font-family:"Montserrat",sans-serif;font-weight:700;font-size:13px;color:var(--blue)}

/* about */
.about{top:1180px;height:410px}
.about-photo{position:absolute;inset:0;background:linear-gradient(90deg,#1f5fa3 0%,#4d80bb 35%,#6f95c2 60%,#2a64a4 100%)}
.about-title{top:50px;font-size:54px;color:var(--white);letter-spacing:1px}
.about-text{left:130px;width:940px;text-align:center;color:var(--white);font-size:16px;line-height:29px}
.about-text.one{top:128px}
.about-text.two{top:200px}
.btn-outline{left:489px;top:284px;width:222px;height:50px;border:1px solid var(--white);color:var(--white);font-size:22px;line-height:48px;text-align:center;letter-spacing:1px}

/* expertise */
.expertise{top:1590px;height:580px;background:linear-gradient(180deg,var(--ice) 0%,var(--sky) 45%,#6f9cca 100%)}
.expertise .section-title{top:52px}
.expertise-core{left:430px;top:150px;width:300px;height:300px;border-radius:50%;background:radial-gradient(circle,#3e78b8 0%,#6f8fb0 55%,rgba(255,255,255,.25) 100%)}
.exp-item{width:240px}
.exp-item h4{font-family:"Montserrat",sans-serif;font-weight:700;font-size:13px;color:var(--white);letter-spacing:.5px}
.exp-item p{margin-top:8px;font-size:12px;line-height:20px;color:var(--white);opacity:.9}
.exp-item.left{text-align:right}
.exp-icon{width:56px;height:56px;border-radius:50%;border:2px solid var(--blue);background:var(--white);display:flex;align-items:center;justify-content:center}

/* team */
.team{top:2170px;height:548px;background:var(--pale)}
.team .section-title{top:50px}
.team-lead{top:102px;left:140px;width:920px;text-align:center;font-size:15px;line-height:27px;color:var(--grey)}
.member{top:190px;width:300px;text-align:center}
.member-photo{width:152px;height:152px;margin:0 auto;border-radius:50%;border:5px solid var(--white);box-shadow:0 1px 6px rgba(0,0,0,.25)}
.member h5{margin-top:20px;font-weight:400;font-size:20px;color:var(--ink)}
.member .role{font-size:16px;color:var(--blue);margin-top:2px}
.member p{margin:12px auto 0;width:250px;font-size:12px;line-height:24px;color:var(--grey)}

/* footer */
.site-footer{top:2718px;height:323px;background:var(--blue);color:var(--white)}
.foot-col{top:42px}
.foot-col h6{font-weight:400;font-size:16px;letter-spacing:.5px;margin-bottom:20px}
.foot-col li{list-style:none;font-size:14px;line-height:30px}
.foot-col li svg{vertical-align:-2px;margin-right:10px}
.foot-divider{top:42px;width:1px;height:170px;background:rgba(255,255,255,.2)}
.social{display:flex;gap:6px;margin-top:10px}
.social span{width:38px;height:38px;border-radius:50%;border:2px solid var(--white);background:#1b9bd8}
.social span:nth-child(2){background:#3b5b9a}
.social span:nth-child(3){background:#1d77b5}
.social span:nth-child(4){background:#d84a38}
.foot-rule{left:100px;top:246px;width:1000px;height:1px;background:rgba(255,255,255,.35)}
.copyright{left:100px;top:272px;font-size:12px}
.foot-code{right:92px;top:272px;font-size:12px}
</style>
</head>
<body>

<header class="site-header">
  <div class="abs brand"><span class="brand-mark"></span><span class="brand-name">Ironvale Energy</span></div>
  <nav class="abs main-nav">
    <a class="active">HOME</a><a>ABOUT</a><a>TEAM</a><a>EXPERTISE</a><a>BLOG</a><a>CONTACT US</a>
  </nav>
</header>

<section class="hero">
  <div class="hero-photo" role="img" aria-label="Businesswoman in a suit standing before a sunlit city skyline"></div>
  <h1 class="abs center hero-title">IRONVALE ENERGY</h1>
  <p class="abs center hero-sub">We conduct consulting to companies and organizations</p>
  <div class="abs btn-solid">GET STARTED NOW</div>
  <div class="abs slider-dots"><span></span><span></span><span></span><span></span></div>
</section>

<section class="welcome">
  <h2 class="abs center section-title">WELCOME TO <em>IRONVALE ENERGY</em></h2>
  <p class="abs welcome-lead">We conduct consulting to companies and organizations working in traditional energy, with an emphasis on community engagement, energy policy, and energy politics.</p>

  <div class="abs card" style="left:100px">
    <div class="card-icon">
      <svg width="56" height="56" viewBox="0 0 56 56" fill="none" stroke="#fff" stroke-width="3" stroke-linecap="round">
        <path d="M28 14a12 12 0 0 0-7 21.7V40h14v-4.3A12 12 0 0 0 28 14z" fill="#fff"/>
        <path d="M22 44h12M24 48h8"/>
        <path d="M28 4v5M12 10l3 3M44 10l-3 3M6 26h4M46 26h4"/>
      </svg>
    </div>
    <h3>TRADITIONAL ENERGY</h3>
    <p>Duis aute irure dolor in reprehenderit in voluptate velit esse cillum dolore eu fugiat nulla pariatur.</p>
    <span class="read-more">READ MORE ➔</span>
  </div>

  <div class="abs card" style="left:446px">
    <div class="card-icon">
      <svg width="64" height="44" viewBox="0 0 64 44" fill="#fff">
        <path d="M2 10l10-4 8 20-10 4z"/><path d="M62 10l-10-4-8 20 10 4z"/>
        <path d="M14 12l12-4h10l12 6-6 14-14 10c-3 2-6 0-5-3l-9-7z" />
      </svg>
    </div>
    <h3>COMMUNITY ENGAGEMENT</h3>
    <p>Sed ut perspiciatis unde omnis iste natus error sit voluptatem accusantium doloremque laudantium rem aperiam.</p>
    <span class="read-more">READ MORE ➔</span>
  </div>

  <div class="abs card" style="left:792px">
    <div class="card-icon">
      <svg width="60" height="54" viewBox="0 0 60 54" fill="none" stroke="#fff" stroke-width="2.5">
        <rect x="8" y="18" width="44" height="24" fill="#fff"/>
        <path d="M8 26h44M8 34h44M19 18v24M30 18v24M41 18v24" stroke="#0255a3" stroke-width="1.5"/>
        <path d="M30 42v8M20 50h20"/>
        <circle cx="30" cy="8" r="4"/>
      </svg>
    </div>
    <h3>ENERGY POLICY AND POLITICS</h3>
    <p>Excepteur sint occaecat cupidatat non proident, sunt in culpa qui officia deserunt mollit anim id est laborum.</p>
    <span class="read-more">READ MORE ➔</span>
  </div>
</section>

<section class="about">
  <div class="about-photo" role="img" aria-label="Two businesswomen in conversation in a bright office, under a blue tint"></div>
  <h2 class="abs center about-title">ABOUT US</h2>
  <p class="abs about-text one">But I must explain to you how all this mistaken idea of denouncing pleasure and praising pain was born and I will give you a complete account of the system, and expound the actual teachings of the great explorer of the truth</p>
  <p class="abs about-text two">Quis autem vel eum iure reprehenderit qui in ea voluptate velit esse quam nihil molestiae consequatur, vel illum qui dolorem eum fugiat quo voluptas nulla pariatur</p>
  <div class="abs btn-outline">READ MORE</div>
</section>

<section class="expertise">
  <h2 class="abs center section-title">OUR <em>EXPERTISE</em></h2>
  <div class="abs expertise-core" role="img" aria-label="Large brand emblem at the centre of the expertise areas"></div>
  <svg class="abs" style="left:0;top:0" width="1200" height="580" fill="none" stroke="#0255a3" stroke-width="1.5">
    <path d="M610 190H716M420 295H442M839 310H760M478 453H600"/>
  </svg>

  <div class="abs exp-icon" style="left:716px;top:130px">
    <svg width="22" height="26" viewBox="0 0 22 26" fill="#0255a3"><path d="M2 1h12l6 6v18H2z"/><path d="M6 12h10M6 16h10M6 20h7" stroke="#fff" stroke-width="2"/></svg>
  </div>
  <div class="abs exp-item" style="left:800px;top:122px"><h4>NAVIGATING POLICY</h4><p>Vestibulum ante ipsum primis in faucibus orci luctus et ultrices posuere cubilia</p></div>

  <div class="abs exp-icon" style="left:364px;top:267px">
    <svg width="28" height="22" viewBox="0 0 28 22" fill="#0255a3"><circle cx="8" cy="6" r="4"/><circle cx="20" cy="6" r="4"/><circle cx="14" cy="9" r="4.5"/><path d="M1 20c0-6 4-8 7-8s5 2 6 2 3-2 6-2 7 2 7 8z"/></svg>
  </div>
  <div class="abs exp-item left" style="left:106px;top:242px"><h4>COMMUNITY ENGAGEMENT</h4><p>Vestibulum ante ipsum primis in faucibus orci luctuset</p></div>

  <div class="abs exp-icon" style="left:783px;top:282px">
    <svg width="20" height="28" viewBox="0 0 20 28" fill="none" stroke="#0255a3" stroke-width="2.2"><path d="M10 2a8 8 0 0 0-5 14v4h10v-4A8 8 0 0 0 10 2z"/><path d="M6 24h8"/></svg>
  </div>
  <div class="abs exp-item" style="left:860px;top:266px"><h4>ENERGY ACCESS</h4><p>Vestibulum ante ipsum primis in faucibus orci luctuset</p></div>

  <div class="abs exp-icon" style="left:422px;top:425px">
    <svg width="26" height="26" viewBox="0 0 26 26" fill="none" stroke="#0255a3" stroke-width="2.5" stroke-linecap="round"><path d="M21 9a9 9 0 0 0-16-1M5 17a9 9 0 0 0 16 1"/><path d="M5 3v5h5M21 23v-5h-5"/></svg>
  </div>
  <div class="abs exp-item left" style="left:162px;top:420px"><h4>DE ESCALATING CONFLICT</h4><p>Vestibulum ante ipsum primis in faucibus orci luctus et ultrices posuere cubilia</p></div>
</section>

<section class="team">
  <h2 class="abs center section-title">OUR <em>TEAM</em></h2>
  <p class="abs team-lead">Sed ut perspiciatis unde omnis iste natus error sit voluptatem accusantium doloremque laudantium, totam rem aperiam, eaque ipsa quae ab illo inventore veritatis et quasi architecto beatae vitae dicta sunt explicabo.</p>

  <div class="abs member" style="left:80px">
    <div class="member-photo" role="img" aria-label="Portrait of consultant Tom Reeler" style="background:radial-gradient(circle at 50% 40%,#cfcfcf,#8a8a8a)"></div>
    <h5>Tom Reeler</h5><div class="role">(Consultant)</div>
    <p>Nemo enim ipsam voluptatem quia voluptas sit aspernatur aut odit aut fugit, sed quia consequuntur magni dolores.</p>
  </div>
  <div class="abs member" style="left:450px">
    <div class="member-photo" role="img" aria-label="Portrait of consultant Owen Marsh" style="background:radial-gradient(circle at 50% 40%,#e6c3a5,#9a7a60)"></div>
    <h5>Owen Marsh</h5><div class="role">(Consultant)</div>
    <p>Nemo enim ipsam voluptatem quia voluptas sit aspernatur aut odit aut fugit, sed quia consequuntur magni dolores.</p>
  </div>
  <div class="abs member" style="left:820px">
    <div class="member-photo" role="img" aria-label="Portrait of consultant Clara Vance" style="background:radial-gradient(circle at 50% 40%,#f1f3f5,#b7cfe0)"></div>
    <h5>Clara Vance</h5><div class="role">(Consultant)</div>
    <p>Nemo enim ipsam voluptatem quia voluptas sit aspernatur aut odit aut fugit, sed quia consequuntur magni dolores.</p>
  </div>
</section>

<footer class="site-footer">
  <div class="abs foot-col" style="left:100px"><h6>COMPANY</h6><ul><li>Home</li><li>About</li><li>Team</li><li>Expertise</li><li>Blog</li></ul></div>
  <div class="abs foot-divider" style="left:222px"></div>
  <div class="abs foot-col" style="left:258px"><h6>SERVICES</h6><ul><li>Traditional Energy</li><li>Community Engagement</li><li>Energy Policy</li><li>Energy Politics</li></ul></div>
  <div class="abs foot-divider" style="left:462px"></div>
  <div class="abs foot-col" style="left:514px"><h6>GET IN TOUCH</h6><ul>
    <li><svg width="14" height="14" viewBox="0 0 14 14" fill="#fff"><path d="M3 1l2 3-1.5 1.5a8 8 0 0 0 5 5L10 9l3 2-1 2.5C6 14 0 8 .5 2z"/></svg>Call us on 0100 555 019</li>
    <li><svg width="14" height="12" viewBox="0 0 14 12" fill="#fff"><path d="M0 1h14v10H0z"/><path d="M0 1l7 5 7-5" stroke="#0255a3" fill="none" stroke-width="1.3"/></svg>info@examplemail.com</li>
  </ul></div>
  <div class="abs foot-divider" style="left:728px"></div>
  <div class="abs foot-col" style="left:768px"><h6>WHY US</h6><ul><li>Customers</li><li>Team</li><li>FAQ</li><li>Contact</li></ul></div>
  <div class="abs foot-divider" style="left:890px"></div>
  <div class="abs foot-col" style="left:929px"><h6>FOLLOW US</h6><ul><li>Please connect with us on</li></ul>
    <div class="social"><span></span><span></span><span></span><span></span></div>
  </div>
  <div class="abs foot-rule"></div>
  <div class="abs copyright">© 2016 Ironvale Energy.&nbsp;&nbsp; All right reserved.&nbsp; Term of Use</div>
  <div class="abs foot-code">C16</div>
</footer>

</body>
</html>
```